Professionell und kommunikativ, kommen gerne wieder.
Zielgruppe
Wir transportieren Güter und Waren aller Art rund um die Welt. Hauptsächlich Luftfracht, aber auch per Schiff und an Land. Hauptsächlich richten wir uns damit an Firmenkunden, weniger an Privatkunden. Für unsere neue Website benötigen wir ein Design.
Aufgabenstellung
Wir benötigen ein Webdesign für den Relaunch unserer Website. Unsere Ideen für unsere neue Website haben wir bereits skizziert (Anlage). Diese Mockups bedürfen nun eines Designs.
Dazu ergänzend gelten die folgenden, formalen Vorgaben:
• 1140px breit, gerne auch Ideen für die Darstellung auf Smartphones und Tablets
• Logo links oben
• Navigation oben waagerecht
• Dropdown-Navigation am Desktop, Hamburger für die mobile Navigation
• Verwendung eines Grid-Systems wie Bootstrap
• Mindestschriftgröße für Mengentext: 16px (bei groß ausfallenden Fonts 15px)
Wir haben keine Hausschriftart und keine festgelegten Farben. Wir möchten aber unser Logo weiterverwenden und da bietet es sich natürlich an, auf dem Rot aufzubauen.

```html
<!DOCTYPE html>
<html lang="en">
<head>
<meta charset="utf-8">
<title>Mobile Navigation</title>
<link rel="stylesheet" href="https://fonts.googleapis.com/css2?family=Arimo:wght@400;700&display=swap">
<style>
  :root {
    --bg: #353535;
    --text: #ffffff;
    --muted: #a3a3a3;
    --divider: #595959;
    --icon-muted: #9a9a9a;
    --accent: #e0070f;
  }
  * { box-sizing: border-box; margin: 0; padding: 0; }
  html, body {
    width: 1200px;
    height: 2641px;
    overflow: hidden;
    background: var(--bg);
  }
  body {
    font-family: "Arimo", Arial, sans-serif;
    color: var(--text);
    position: relative;
  }
  .menu-title {
    position: absolute;
    left: 77px;
    top: 136px;
    font-size: 83px;
    font-weight: 700;
    line-height: 1;
  }
  .menu-close {
    position: absolute;
    left: 1058px;
    top: 89px;
    width: 56px;
    height: 56px;
  }
  .nav-list {
    position: absolute;
    left: 77px;
    top: 360px;
    width: 1046px;
    list-style: none;
  }
  .nav-item {
    height: 257px;
    display: flex;
    align-items: center;
    justify-content: space-between;
    font-size: 67px;
    font-weight: 700;
    border-bottom: 3px solid var(--divider);
  }
  .nav-item:last-child { border-bottom: none; }
  .nav-item + .nav-item { height: 257px; }
  .nav-list .nav-item:nth-child(2) { height: 257px; }
  .nav-chevron { width: 40px; height: 70px; margin-right: 8px; }
  .quote-button {
    position: absolute;
    left: 77px;
    top: 1951px;
    width: 1046px;
    height: 157px;
    background: var(--accent);
    display: flex;
    align-items: center;
    justify-content: center;
    font-size: 45px;
    font-weight: 700;
    letter-spacing: 0.5px;
  }
  .contact-row {
    position: absolute;
    left: 77px;
    display: flex;
    align-items: center;
  }
  .contact-row.phone { top: 2233px; }
  .contact-row.mail { top: 2438px; }
  .contact-icon { width: 100px; height: 100px; }
  .contact-text { margin-left: 51px; }
  .contact-label {
    font-size: 37px;
    font-weight: 700;
    color: var(--muted);
    letter-spacing: 3px;
    line-height: 1.15;
  }
  .contact-value {
    font-size: 48px;
    font-weight: 700;
    letter-spacing: 2px;
    line-height: 1.2;
  }
</style>
</head>
<body>
  <h1 class="menu-title">Menu</h1>
  <svg class="menu-close" viewBox="0 0 56 56" aria-label="Close menu">
    <path d="M4 4 L52 52 M52 4 L4 52" stroke="var(--icon-muted)" stroke-width="5" fill="none"/>
  </svg>

  <ul class="nav-list">
    <li class="nav-item">Services
      <svg class="nav-chevron" viewBox="0 0 40 70"><path d="M6 4 L34 35 L6 66" stroke="var(--text)" stroke-width="5" fill="none"/></svg>
    </li>
    <li class="nav-item">About us</li>
    <li class="nav-item">Contact us</li>
  </ul>

  <div class="quote-button">GET A QUOTE</div>

  <div class="contact-row phone">
    <svg class="contact-icon" viewBox="0 0 100 100" aria-label="Phone">
      <path d="M22 8 L36 22 C39 25 39 29 36 32 L30 38 C36 52 48 64 62 70 L68 64 C71 61 75 61 78 64 L92 78 C94 80 94 83 92 85 L84 93 C80 97 72 98 62 93 C40 82 18 60 7 38 C2 28 3 20 7 16 L15 8 C17 6 20 6 22 8 Z" stroke="var(--text)" stroke-width="5" fill="none" stroke-linejoin="round"/>
      <path d="M58 22 A22 22 0 0 1 78 42 M60 6 A38 38 0 0 1 94 40" stroke="var(--text)" stroke-width="5" fill="none" stroke-linecap="round"/>
    </svg>
    <div class="contact-text">
      <div class="contact-label">CALL US</div>
      <div class="contact-value">+49 321 / 654 987 00</div>
    </div>
  </div>

  <div class="contact-row mail">
    <svg class="contact-icon" viewBox="0 0 100 100" aria-label="Mail">
      <path d="M94 6 L4 44 L38 58 L50 94 Z M94 6 L38 58" stroke="var(--text)" stroke-width="5" fill="none" stroke-linejoin="round"/>
    </svg>
    <div class="contact-text">
      <div class="contact-label">SEND US A MAIL</div>
      <div class="contact-value">INFO@SKYLANEFREIGHT.COM</div>
    </div>
  </div>
</body>
</html>
```